Software Company Business Card Design

We are looking for a business card design for a software, messaging & IT services company based in Australia.

Lumora Group is the holding company for 3 brands all offering technology based business solutions; Lumora, Velbrix & Quillray. Brand Identity = Friendly, Professional, Viable, Vibrant, Creative

We want our business card to reflect that we are an innovative market leader. The design should be clean, professional and original.

This design will be used for all 3 brands.

More information about our company can be found at: www.lumoragroup-example.com.au
www.velbrix-example.com.au

Details we would like on the card:

Firstname Lastname
Position
Level 17, 248 Tarrow St
North Sydney
NSW 2060
Phone: +61 2 9387 2600
Fax: +61 2 9387 2611
Mobile:
Email:
www.lumoragroup-example.com.au

Target Market(s)

Our business cards are given to B2B and industry professionals.

Industry/Entity Type

Business

Requirements
Must have
• The Business Card must include the same colours as the logo.
Nice to have
• We would like it to me double sided.

```html
<!DOCTYPE html>
<html lang="en">
<head>
<meta charset="utf-8">
<title>Lumora Group – Business Card</title>
<link rel="stylesheet" href="https://fonts.googleapis.com/css2?family=Cabin:wght@400;500;600&display=swap">
<style>
  :root {
    --page-bg: #e9e9e9;
    --card-bg: #303030;
    --brand-crimson: #c0103f;
    --text-white: #ffffff;
    --text-lavender: #a9a3d4;
  }
  * { margin: 0; padding: 0; box-sizing: border-box; }
  html, body {
    width: 1200px;
    height: 1200px;
    overflow: hidden;
    background: var(--page-bg);
    font-family: "Cabin", sans-serif;
  }
  .canvas {
    position: relative;
    width: 1200px;
    height: 1200px;
  }
  .card {
    position: absolute;
    top: 374px;
    width: 562px;
    height: 337px;
    background: var(--card-bg);
  }
  .card--front { left: 33px; }
  .card--back { left: 604px; }

  .brand-mark {
    position: absolute;
    left: 140px;
    top: 508px;
    width: 136px;
    display: flex;
    flex-direction: column;
    align-items: center;
    gap: 12px;
  }
  .brand-mark__dot {
    width: 96px;
    height: 96px;
    border-radius: 50%;
    background: var(--brand-crimson);
  }
  .brand-mark__name {
    color: var(--brand-crimson);
    font-weight: 600;
    font-size: 22px;
    letter-spacing: 0.5px;
  }

  .contact {
    position: absolute;
    left: 306px;
    top: 512px;
    color: var(--text-white);
  }
  .contact__name {
    font-size: 25px;
    font-weight: 600;
    line-height: 30px;
  }
  .contact__position {
    font-size: 18px;
    font-weight: 500;
    color: var(--text-lavender);
    line-height: 20px;
  }
  .contact__lines {
    margin-top: 12px;
    font-size: 18px;
    font-weight: 500;
    line-height: 23px;
  }
  .contact__address {
    font-size: 14.5px;
    line-height: 19px;
    margin-top: 2px;
  }
  .contact__label { font-size: 18px; }

  .wordmark {
    position: absolute;
    left: 604px;
    top: 374px;
    width: 562px;
    height: 337px;
    display: flex;
    align-items: center;
    justify-content: center;
    color: var(--brand-crimson);
    font-weight: 600;
    font-size: 52px;
    letter-spacing: 0.5px;
  }
</style>
</head>
<body>
<main class="canvas">
  <section class="card card--front" aria-label="Card front"></section>
  <div class="brand-mark">
    <span class="brand-mark__dot"></span>
    <span class="brand-mark__name">Lumora</span>
  </div>
  <div class="contact">
    <p class="contact__name">Firstname Lastname</p>
    <p class="contact__position">position</p>
    <div class="contact__lines">
      <p>P: +61 2 9387 2600</p>
      <p>F: +61 2 9387 2611</p>
      <p class="contact__address"><span class="contact__label">A:</span> Level 17, 248 Tarrow St North<br>Sydney NSW 2060</p>
    </div>
  </div>

  <section class="card card--back" aria-label="Card back"></section>
  <div class="wordmark">Lumora Group</div>
</main>
</body>
</html>
```